Full Page Ad for Coastal Dwelling Journal

we are The Garden Quarter an Outdoor design and construction company form Miami. see our website to get a better idea of who we are, what we do and our company profile. www.thegardenquarter-example.com

we need a full page ad for a luxury construction an architecture magazine. see magazine profile http://www.coastaldwelling-example.com/

design requirements:

use a minimum of 1 images or a maximum of 4 images from the files available

include Logo ( obviously )

include following text ( in no particular order):
"Outdoor Design & Construction / Outdoor Furniture "
"we create unique outdoor living spaces"
"thegardenquarter-example.com"
"Showroom: 4120 NW 62 Ave Miami, FL 33166"
"786.555.0142"

From the files uploaded see examples of ads that we like.

Specs:
Full Page
Final Trim : 8" x 10-7/8"
Live Area ( type) 7" x 10"
Bleed: 8.25" x 11.125"
Decimal equivalents: 8" x 10.875"

Reason: Really like the designs guys just want to see a few more options using some of the images that haven't been used yet. particularly the white structure attached to the house. thanks, TGQ Marketing team

```html
<!DOCTYPE html>
<html lang="en">
<head>
<meta charset="utf-8">
<title>The Garden Quarter — Full Page Ad</title>
<link rel="stylesheet" href="https://fonts.googleapis.com/css2?family=Barlow:wght@500;600&family=Arimo&display=swap">
<style>
  :root {
    --gold: #f2c200;
    --amber: #e8a000;
    --orange: #f26a1a;
    --ember: #c8461c;
    --brown-dark: #2a1606;
    --cyan: #16d8ff;
    --blue: #0a6ad8;
    --navy-dark: #04111f;
    --paper: #ffffff;
    --ink: #111111;
    --logo-blue: #2f6fb3;
    --photo-garden: #5d7a4a;
    --photo-terrace: #c9d6df;
  }
  html, body {
    margin: 0;
    padding: 0;
    overflow: hidden;
    background: var(--paper);
  }
  .ad {
    position: relative;
    width: 889px;
    height: 1200px;
    overflow: hidden;
    background: var(--paper);
  }
  .hero {
    position: absolute;
    left: 0; top: 0;
    width: 889px; height: 805px;
    background:
      radial-gradient(ellipse 260px 420px at 40px 330px, rgba(242,194,0,0.55), transparent 70%),
      radial-gradient(ellipse 260px 480px at 860px 330px, rgba(10,106,216,0.35), transparent 70%),
      linear-gradient(90deg, #8a6400 0%, #5a3a08 22%, var(--brown-dark) 50%, #061a33 58%, var(--navy-dark) 100%);
  }
  .hero::after {
    content: "";
    position: absolute;
    inset: 0;
    background: linear-gradient(180deg, rgba(0,0,0,0.35) 0%, rgba(0,0,0,0) 30%, rgba(0,0,0,0.25) 100%);
  }
  .headline {
    position: absolute;
    left: 0; top: 76px;
    width: 889px;
    margin: 0;
    z-index: 1;
    text-align: center;
    font-family: "Barlow", sans-serif;
    font-weight: 500;
    font-size: 112px;
    line-height: 103px;
    letter-spacing: 2px;
    text-transform: uppercase;
    background: linear-gradient(90deg, var(--gold) 0%, var(--amber) 25%, var(--orange) 40%, var(--ember) 52%, #e0602a 57%, var(--cyan) 60%, var(--cyan) 100%);
    -webkit-background-clip: text;
    background-clip: text;
    color: transparent;
    filter: drop-shadow(2px 3px 2px rgba(0,0,0,0.7));
  }
  .headline span { display: block; }
  .services {
    position: absolute;
    left: 0; top: 726px;
    width: 889px;
    margin: 0;
    z-index: 1;
    text-align: center;
    font-family: "Barlow", sans-serif;
    font-weight: 500;
    font-size: 27px;
    line-height: 31px;
    letter-spacing: 1px;
    text-transform: uppercase;
    background: linear-gradient(90deg, var(--gold) 0%, #f7e600 55%, #ffffff 58%, var(--cyan) 70%, var(--cyan) 100%);
    -webkit-background-clip: text;
    background-clip: text;
    color: transparent;
  }
  .services span { display: block; }
  .gallery {
    position: absolute;
    left: 0; top: 805px;
    width: 889px; height: 330px;
  }
  .brand {
    position: absolute;
    left: 331px; top: 838px;
    width: 258px; height: 258px;
    border-radius: 50%;
    background: var(--paper);
    display: flex;
    align-items: center;
    justify-content: center;
    text-align: center;
    font-family: "Barlow", sans-serif;
    font-weight: 600;
    font-size: 30px;
    line-height: 34px;
    color: var(--logo-blue);
    text-transform: uppercase;
  }
  .contact {
    position: absolute;
    left: 0; top: 1141px;
    width: 889px;
    text-align: center;
    font-family: "Arimo", sans-serif;
    font-size: 15.5px;
    line-height: 21px;
    color: var(--ink);
  }
  .contact p { margin: 0; }
</style>
</head>
<body>
  <main class="ad">
    <section class="hero">
      <h1 class="headline">
        <span>We</span>
        <span>Create</span>
        <span>Unique</span>
        <span>Outdoor</span>
        <span>Living</span>
        <span>Spaces</span>
      </h1>
      <p class="services">
        <span>Outdoor Design &amp; Construction</span>
        <span>Outdoor Furniture</span>
      </p>
    </section>

    <svg class="gallery" viewBox="0 0 889 330" xmlns="http://www.w3.org/2000/svg">
      <defs>
        <linearGradient id="garden-tones" x1="0" y1="0" x2="0" y2="1">
          <stop offset="0" stop-color="#a9c4d6"/>
          <stop offset="0.35" stop-color="#6f8a4e"/>
          <stop offset="0.7" stop-color="#4a4030"/>
          <stop offset="1" stop-color="#2b3338"/>
        </linearGradient>
        <linearGradient id="terrace-tones" x1="0" y1="0" x2="1" y2="1">
          <stop offset="0" stop-color="#6fb2e6"/>
          <stop offset="0.35" stop-color="#e9eef1"/>
          <stop offset="1" stop-color="#b9c4cc"/>
        </linearGradient>
      </defs>
      <polygon role="img" aria-label="Photo: Miami home backyard with palm trees, pergola, green loungers and a dark reflecting pool"
               points="0,10 365,10 505,328 0,328" fill="url(#garden-tones)"/>
      <polygon role="img" aria-label="Photo: white louvered aluminium pergola attached to the house, with white lounge seating on a marble terrace by the sea"
               points="373,10 889,10 889,328 513,328" fill="url(#terrace-tones)"/>
    </svg>

    <div class="brand">The Garden<br>Quarter</div>

    <footer class="contact">
      <p>thegardenquarter-example.com</p>
      <p>Showroom: 4120 NW 62 Ave Miami, FL 33166 | 786.555.0142</p>
    </footer>
  </main>
</body>
</html>
```